Electrical & Communications Company Wordpress Themed Website Design

Hi everyone,

I need a wordpress themed website designed for a new company based in Sydney Australia called "TRELVEX". It delivers electrical and communication services to the domestic and commercial sectors.

It needs to be the FULL/COMPLETE wordpress theme! A clean and easy to use site.

Please guys take the time to look at these competitors sites:

www.quobble.com.au
www.zirconvoltworks.com.au
www.ubt.com.au
www.tallowwiring.com.au
www.wrightbergwire.com.au
www.gullivarwiremen.com.au

Please use these site for ideas only!!! we want to be original.

(If you would like to add electrical and communications to the logo that is O.K.)

Note: These logo's are registered trademarks of trelvex pty ltd.

Accreditation:

Bufo member (United cabling and signalling trades guild)

PLEASE CHECK THE WEB PLANNING LAYOUT BELOW FOR ROUGH IDEA

Have requested to increase payment to $400 and now guarantee payment!

Hi guys, forgot to mention i would like to see the business phone number prominently some where with a call to action.As we are a service business and need people to easly be able to see our contact number. Maybe top right courner but open to ideas. 

 Guys/Girls this is for a complete working word press theme that i can load up on the sever and access thru wordpress admin. Code etc

• - Logo Provided must be used
• - Themes and colours to be consisted with with brand
• - Fully customizable
• - Have a social share button from pinquo.com
• - Must be the full/complete theme for word press
• - zenpixbanks
• - contactform
• - would like orbe lumo charge bitfen displayed
• - Guarantee logo or something
• - Please don't waste your or our time submitting templates or copies of other sites original only!

```html
<!DOCTYPE html>
<html lang="en">
<head>
<meta charset="utf-8">
<title>TRELVEX – Electrical &amp; Communications</title>
<link href="https://fonts.googleapis.com/css2?family=Arimo:wght@400;700&display=swap" rel="stylesheet">
<style>
:root{
  --red:#ec1c24;
  --dark:#444446;
  --tab:#5a5a5c;
  --text:#333;
  --muted:#9a9a9a;
  --photo-a:#d9d9d9;
  --photo-b:#8c8c8c;
  --white:#fff;
}
*{box-sizing:border-box;margin:0;padding:0}
html,body{width:891px;height:1200px;overflow:hidden;background:var(--white)}
body{position:relative;font-family:"Arimo",Arial,sans-serif;color:var(--text)}
h2,h3{font-weight:400}
.abs{position:absolute}
/* header */
.brand-block{left:33px;top:47px;width:26px;height:45px;background:var(--red)}
.brand-name{left:70px;top:50px;display:flex;align-items:center;gap:10px;font-size:46px;font-weight:700;color:var(--red);letter-spacing:1px;line-height:40px}
.brand-name .dot{width:18px;height:18px;border-radius:50%;background:var(--red)}
.brand-bar{left:346px;top:47px;width:514px;height:45px;background:var(--red)}
.main-nav{position:absolute;left:0;top:0;z-index:2}
.nav-tab{position:absolute;top:102px;height:19px;color:var(--white);font-size:14px;line-height:19px;text-align:center;text-decoration:none;z-index:1}
.nav-tab::before{content:"";position:absolute;inset:0;background:var(--tab);transform:skewX(-28deg);z-index:-1}
.nav-tab.is-italic{font-style:italic}
/* hero */
.hero{left:33px;top:133px;width:827px;height:176px;background:linear-gradient(100deg,#7d7d7d 0%,#c9c9c9 35%,#e4e4e4 70%,#bdbdbd 100%)}
.cta{left:461px;top:155px;width:372px;height:127px;background:rgba(240,240,240,.9)}
.cta-title{left:30px;top:24px;font-size:19px;font-weight:700;letter-spacing:2px;color:var(--red)}
.cta-text{left:30px;top:54px;font-size:19px;line-height:18px;color:#555;letter-spacing:.5px}
.cta-button{left:258px;top:66px;width:90px;height:28px;background:#111;border:1px solid #000;box-shadow:inset 0 0 0 1px #666;color:var(--white);font-size:18px;line-height:26px;text-align:center;letter-spacing:.5px}
/* service tiles */
.tile{position:absolute;top:326px;width:200px}
.tile-head{height:23px;background:var(--red);color:var(--white);font-size:18px;line-height:24px;padding-left:9px;letter-spacing:.3px}
.tile-photo{height:78px;margin-top:4px;background:linear-gradient(135deg,var(--photo-a),var(--photo-b))}
.tile-sub{margin-top:14px;font-size:12px;font-weight:700;letter-spacing:.5px;color:#111}
.tile-body{margin-top:4px;width:199px;font-size:9.6px;line-height:17.4px;letter-spacing:.5px;color:#444}
.read-more{display:flex;align-items:center;gap:5px;font-size:9.8px;font-weight:700;color:#111;letter-spacing:.3px}
.tile .read-more{position:absolute;right:3px;top:267px}
.tile-rule{position:absolute;top:291px;left:0;width:200px;height:5px;background:var(--dark)}
/* sections */
.section-title{font-size:19px;color:var(--red);letter-spacing:.5px}
.news{position:absolute;left:33px;width:410px}
.news-date{font-size:9px;color:var(--muted);letter-spacing:.5px}
.news-title{margin-top:6px;font-size:12.5px;font-weight:700;color:#111;letter-spacing:.4px}
.news-body{margin-top:2px;width:388px;font-size:9.6px;line-height:17.4px;letter-spacing:.45px;color:#444}
.news .read-more{margin-top:3px}
.project{position:absolute;left:451px;width:409px}
.project-photo{position:absolute;left:0;top:0;width:113px;height:78px;background:linear-gradient(135deg,var(--photo-a),var(--photo-b))}
.project-title{position:absolute;left:130px;top:0;font-size:12.5px;font-weight:700;color:#111;letter-spacing:.4px}
.project-body{position:absolute;left:130px;top:22px;width:279px;font-size:9.6px;line-height:17.4px;letter-spacing:.3px;color:#444}
.project .read-more{position:absolute;right:3px}
/* footer */
.footer{left:33px;top:982px;width:827px;height:174px;background:var(--dark);color:var(--white)}
.footer-title{position:absolute;top:14px;font-size:19px;letter-spacing:.3px}
.footer-list{position:absolute;top:58px;width:208px;list-style:none}
.footer-list li{display:flex;align-items:center;gap:9px;height:24.5px;border-bottom:1px solid #8a8a8a;font-size:11.5px;padding-left:4px;letter-spacing:.3px}
.footer-brand{position:absolute;left:611px;top:56px;font-size:26px;font-weight:700;letter-spacing:1px}
.footer-address{position:absolute;left:617px;top:103px;font-size:9.8px;line-height:17.4px;letter-spacing:.4px;font-style:normal}
.partner-badge{position:absolute;left:766px;top:120px;width:46px;height:30px;border-radius:3px;background:#d8d8d8}
.legal{top:1179px;left:33px;width:827px;display:flex;justify-content:space-between;font-size:9.5px;color:#333}
.legal nav a{color:#333;text-decoration:none}
.legal nav span{margin:0 7px;color:#888}
</style>
</head>
<body>

<header>
  <div class="abs brand-block"></div>
  <div class="abs brand-name"><span class="dot"></span>TRELVEX</div>
  <div class="abs brand-bar"></div>
  <nav class="main-nav">
    <a class="nav-tab is-italic" style="left:339px;width:96px">Home</a>
    <a class="nav-tab is-italic" style="left:444px;width:96px">Services</a>
    <a class="nav-tab is-italic" style="left:548px;width:100px">About us</a>
    <a class="nav-tab" style="left:653px;width:100px">Quotes</a>
    <a class="nav-tab" style="left:758px;width:100px">Contact</a>
  </nav>
</header>

<section class="abs hero" role="img" aria-label="Close-up photograph of electrical wiring and terminal blocks"></section>
<div class="abs cta">
  <div class="abs cta-title">CALL TO ACTION</div>
  <div class="abs cta-text">Lorem ipsum dolar sit<br>amet avec deo lorem</div>
  <div class="abs cta-button">Call us</div>
</div>

<svg width="0" height="0" style="position:absolute">
  <symbol id="icon-plus" viewBox="0 0 12 12"><circle cx="6" cy="6" r="5" fill="none" stroke="#111" stroke-width="1.2"/><path d="M6 3.2v5.6M3.2 6h5.6" stroke="#111" stroke-width="1.4"/></symbol>
  <symbol id="icon-arrow" viewBox="0 0 14 14"><circle cx="7" cy="7" r="7" fill="#fff"/><path d="M3.5 7h6M7 4.3 9.8 7 7 9.7" fill="none" stroke="#444446" stroke-width="1.8"/></symbol>
</svg>

<section class="services">
  <article class="tile" style="left:33px">
    <div class="tile-head">SERVICE TILE</div>
    <div class="tile-photo" role="img" aria-label="Photograph of hands using wire strippers"></div>
    <div class="tile-sub">Service subtitle</div>
    <p class="tile-body">Lorem Ipsum is simply dummy text of the printing and typesetting industry. Lorem Ipsum has been the industry's standard dummy text ever since the 1500s, when an unknown printer took a galley of type and scrambled it to make a type specimen book.</p>
    <div class="read-more"><svg width="11" height="11"><use href="#icon-plus"/></svg>read more</div>
    <div class="tile-rule"></div>
  </article>
  <article class="tile" style="left:242px">
    <div class="tile-head">SERVICE TILE</div>
    <div class="tile-photo" role="img" aria-label="Photograph of a wired switchboard"></div>
    <div class="tile-sub">Service subtitle</div>
    <p class="tile-body">Lorem Ipsum is simply dummy text of the printing and typesetting industry. Lorem Ipsum has been the industry's standard dummy text ever since the 1500s, when an unknown printer took a galley of type and scrambled it to make a type specimen book.</p>
    <div class="read-more"><svg width="11" height="11"><use href="#icon-plus"/></svg>read more</div>
    <div class="tile-rule"></div>
  </article>
  <article class="tile" style="left:451px">
    <div class="tile-head">SERVICE TILE</div>
    <div class="tile-photo" role="img" aria-label="Photograph of a chandelier light fitting"></div>
    <div class="tile-sub">Service subtitle</div>
    <p class="tile-body">Lorem Ipsum is simply dummy text of the printing and typesetting industry. Lorem Ipsum has been the industry's standard dummy text ever since the 1500s, when an unknown printer took a galley of type and scrambled it to make a type specimen book.</p>
    <div class="read-more"><svg width="11" height="11"><use href="#icon-plus"/></svg>read more</div>
    <div class="tile-rule"></div>
  </article>
  <article class="tile" style="left:660px">
    <div class="tile-head">SERVICE TILE</div>
    <div class="tile-photo" role="img" aria-label="Photograph of electrical plans and tools"></div>
    <div class="tile-sub">Service subtitle</div>
    <p class="tile-body">Lorem Ipsum is simply dummy text of the printing and typesetting industry. Lorem Ipsum has been the industry's standard dummy text ever since the 1500s, when an unknown printer took a galley of type and scrambled it to make a type specimen book.</p>
    <div class="read-more"><svg width="11" height="11"><use href="#icon-plus"/></svg>read more</div>
    <div class="tile-rule"></div>
  </article>
</section>

<h2 class="abs section-title" style="left:33px;top:678px">RECENT NEWS</h2>
<h2 class="abs section-title" style="left:451px;top:678px">FEATURED PROJECTS</h2>

<article class="news" style="top:712px">
  <div class="news-date">9/1/2010</div>
  <h3 class="news-title">News item title goes here</h3>
  <p class="news-body">Lorem Ipsum is simply dummy text of the printing and typesetting industry. Lorem Ipsum has been the industry's standard dummy text ever since the 1500s, when an unknown</p>
  <div class="read-more"><svg width="11" height="11"><use href="#icon-plus"/></svg>read more</div>
</article>
<article class="news" style="top:834px">
  <div class="news-date">9/1/2010</div>
  <h3 class="news-title">News item title goes here</h3>
  <p class="news-body">Lorem Ipsum is simply dummy text of the printing and typesetting industry. Lorem Ipsum has been the industry's standard dummy text ever since the 1500s, when an unknown printer took a ...</p>
  <div class="read-more"><svg width="11" height="11"><use href="#icon-plus"/></svg>read more</div>
</article>

<article class="project" style="top:721px">
  <div class="project-photo" role="img" aria-label="Photograph of hands using wire strippers"></div>
  <h3 class="project-title">Project title goes here</h3>
  <p class="project-body">Lorem Ipsum is simply dummy text of the printing and type-setting industry. Lorem Ipsum has been the industry's stan-dard dummy text ever since the 1500s, when an unknown</p>
  <div class="read-more" style="top:80px"><svg width="11" height="11"><use href="#icon-plus"/></svg>read more</div>
</article>
<article class="project" style="top:843px">
  <div class="project-photo" role="img" aria-label="Photograph of hands using wire strippers"></div>
  <h3 class="project-title">Project title goes here</h3>
  <p class="project-body">Lorem Ipsum is simply dummy text of the printing and type-setting industry. Lorem Ipsum has been the industry's stan-dard dummy text ever since the 1500s, when an unknown</p>
  <div class="read-more" style="top:90px"><svg width="11" height="11"><use href="#icon-plus"/></svg>read more</div>
</article>

<footer class="abs footer">
  <h2 class="footer-title" style="left:25px">Recent posts</h2>
  <ul class="footer-list" style="left:28px">
    <li><svg width="13" height="13"><use href="#icon-arrow"/></svg>Post&nbsp; title goes here</li>
    <li><svg width="13" height="13"><use href="#icon-arrow"/></svg>Another goes here</li>
    <li><svg width="13" height="13"><use href="#icon-arrow"/></svg>Another post product goes her</li>
    <li><svg width="13" height="13"><use href="#icon-arrow"/></svg>Popular post title goes here</li>
  </ul>
  <h2 class="footer-title" style="left:338px;top:16px">Archive</h2>
  <ul class="footer-list" style="left:338px">
    <li><svg width="13" height="13"><use href="#icon-arrow"/></svg>August 2010</li>
    <li><svg width="13" height="13"><use href="#icon-arrow"/></svg>July 2010</li>
    <li><svg width="13" height="13"><use href="#icon-arrow"/></svg>June 2010</li>
    <li><svg width="13" height="13"><use href="#icon-arrow"/></svg>2009</li>
  </ul>
  <div class="footer-brand">TRELVEX</div>
  <address class="footer-address">Trelvex Electric Co Inc<br>48 Harbour Lane<br>Parramatta, NSW 2150</address>
  <div class="partner-badge" aria-label="Trade association member badge"></div>
</footer>

<div class="abs legal">
  <nav><a>Home</a><span>|</span><a>About us</a><span>|</span><a>Services</a><span>|</span><a>Products</a><span>|</span><a>News</a><span>|</span><a>Sitemap</a><span>|</span><a>Contact us</a></nav>
  <div>(c) Copyright 2010 Trelvex. All rights reserved.</div>
</div>

</body>
</html>
```